I would like alternative creative proposals for our website header at mirrowenhaven.com.au
The current is seen as a bit too drab and dark. We would like to liven it up a bit. The logo will remain although we are open to alternative representation or styling. All submitted designs should include a version that has the existing logo (we do use it within a black circle in other marketing).
The fundamental features of the header must be present including brand logo, search, cart etc.
We want to expand our concept of how the header could appear and function and how it represents our business. Other web site expects will be redesigned to align.
Please become familiar with our business and what we are trying to achieve before submitting a design. We are about health, organic products, chemical free low toxin living, environmental sustainability, all delivered in a modern socially friendly way accessible to all demographics and walks of life with our primary focus on Australia. Our primary target demographic is Australian women between 35 and 55. If you would like more info then please send us some questions.
Development and full design is outside the scoop of this proposal. We are looking for "mockup" proposals for the new website header initially.

```html
<!DOCTYPE html>
<html lang="en">
<head>
<meta charset="utf-8">
<title>Mirrowen Haven – Header</title>
<link rel="stylesheet" href="https://fonts.googleapis.com/css2?family=Cabin:ital,wght@0,400;0,600;1,600&family=Cabin+Condensed:wght@400;500&display=swap">
<style>
  :root {
    --bar-green: #2f5d46;
    --bar-text: #f3efe3;
    --ink: #23362c;
    --rule: #2f5d46;
    --cream: #f7f2e6;
    --sage: #dfe9dc;
    --leaf: #3f7a5a;
    --leaf-soft: #a9c8a4;
    --bloom: #e58a45;
    --bloom-soft: #f6c89c;
    --field: #ffffff;
  }
  * { box-sizing: border-box; margin: 0; padding: 0; }
  html, body { width: 1200px; height: 250px; overflow: hidden; background: var(--cream); }
  .site-header {
    position: relative; width: 1200px; height: 250px; overflow: hidden;
    font-family: "Cabin", sans-serif; color: var(--ink);
  }
  .contact-bar {
    position: absolute; left: 0; top: 0; width: 1200px; height: 23px;
    background: var(--bar-green); color: var(--bar-text); font-size: 12px;
  }
  .contact-bar .phone { position: absolute; left: 42px; top: 4px; }
  .contact-bar .email { position: absolute; left: 200px; top: 4px; }
  .social-links { position: absolute; right: 12px; top: 5px; display: flex; gap: 11px; }
  .social-links span { width: 13px; height: 13px; border-radius: 50%; background: var(--bar-text); }
  .hero-photo {
    position: absolute; left: 0; top: 23px; width: 1200px; height: 227px;
    background:
      radial-gradient(ellipse 70px 110px at 1170px 120px, var(--bloom-soft), transparent 72%),
      radial-gradient(ellipse 45px 100px at 605px 95px, var(--leaf-soft), transparent 72%),
      radial-gradient(ellipse 40px 60px at 590px 215px, #e8c9ad, transparent 72%),
      linear-gradient(90deg, var(--cream) 0 406px, var(--sage) 406px 800px, var(--cream) 800px);
  }
  .brand {
    position: absolute; left: 22px; top: 88px; display: flex; align-items: center; gap: 8px;
    font-weight: 600; font-size: 19px; color: var(--leaf); line-height: 1;
  }
  .brand .dot { width: 16px; height: 16px; border-radius: 50%; background: var(--bloom); }
  .account-links { position: absolute; left: 0; top: 0; font-size: 13.6px; letter-spacing: .3px; }
  .account-links a { position: absolute; color: var(--ink); text-decoration: none; white-space: nowrap; }
  .account-links .cart { color: var(--bloom); font-weight: 600; }
  .search-box {
    position: absolute; left: 892px; top: 122px; width: 220px; height: 26px;
    background: var(--field); border-radius: 13px; border: 1px solid var(--leaf-soft);
  }
  .search-box span {
    position: absolute; left: 12px; top: 7px; font-size: 8px; font-weight: 600; font-style: italic; color: var(--ink);
  }
  .search-box svg { position: absolute; right: 10px; top: 6px; }
  .main-nav { position: absolute; left: 0; top: 167px; width: 1200px; height: 26px;
    font-family: "Cabin Condensed", sans-serif; font-size: 12.4px; font-weight: 500; }
  .main-nav a { position: absolute; top: 0; color: var(--ink); text-decoration: none; white-space: nowrap; }
  .main-nav .active { color: var(--leaf); }
  .main-nav .active::after {
    content: ""; position: absolute; left: -12px; right: -12px; top: 22px; height: 3px;
    background: var(--bloom); border-radius: 2px;
  }
  .nav-rule { position: absolute; left: 8px; top: 192px; width: 1184px; height: 1px; background: var(--rule); }
</style>
</head>
<body>
<header class="site-header">
  <div class="hero-photo" role="img" aria-label="Photo of a hand holding a small green leafy sprig against a pale wall, with orange flowers at the right edge"></div>

  <div class="contact-bar">
    <span class="phone">Ph: 02 5550 1847</span>
    <span class="email">mail:info@mirrowenhaven.com.au</span>
    <div class="social-links" aria-label="Social links"><span></span><span></span><span></span><span></span></div>
  </div>

  <div class="brand"><span class="dot"></span>Mirrowen Haven</div>

  <nav class="account-links" aria-label="Account">
    <a style="left:893px;top:58px">COMPARE</a>
    <a style="left:970px;top:58px">BLOG</a>
    <a style="left:1022px;top:56px">LOGIN</a>
    <a style="left:1078px;top:56px">JOIN</a>
    <a style="left:1022px;top:79px">MY ACCOUNT</a>
    <a class="cart" style="left:1050px;top:101px">MY CART</a>
  </nav>

  <div class="search-box">
    <span>Search here ...</span>
    <svg width="12" height="12" viewBox="0 0 12 12" aria-hidden="true">
      <circle cx="4.5" cy="4.5" r="3.3" fill="none" stroke="#2f5d46" stroke-width="1.5"/>
      <line x1="7" y1="7" x2="11" y2="11" stroke="#2f5d46" stroke-width="2"/>
    </svg>
  </div>

  <nav class="main-nav" aria-label="Main">
    <a class="active" style="left:170px">FRESH</a>
    <a style="left:238px">FOOD &amp; DRINK</a>
    <a style="left:346px">HEALTH &amp; HYGIENE</a>
    <a style="left:481px">SKIN, HAIR &amp; BODY</a>
    <a style="left:620px">MUM &amp; BUB</a>
    <a style="left:722px">YOGA &amp; WELLBEING</a>
    <a style="left:866px">ECO TOXIN FREE LIVING</a>
    <a style="left:1032px">ECO CLOTHING</a>
  </nav>
  <div class="nav-rule"></div>
</header>
</body>
</html>
```